Website/Logo Design

We need a logo and website design for an opinion mining startup called VantaLume. Our technology mines the web to automatically discover what people are saying about brands, products, etc. The project we are fielding here is for our informational, public-facing website. In its initial incarnation, it will simply be a vehicle for marketing materials and information on our company and its offerings, but it should be flexible enough to expand as more content/functionality is added.

Some designs we like are:
http://www.tradewhisk.example
http://www.gorvantel.example
http://www.kfz.example
http://www.lintwharf.example
http://moxbarrel.example
http://trundlemq.example
http://www.zopla.example
Updates

All, please try to shy away from using a photo of a person as the focal point of the design.  Our company is more technological than social.

Target Market(s)

Primarily businesses interested in sentiment analysis (typically companies involved in advertising, market research, PR, etc.)

Industry/Entity Type

It Company

Requirements
Must have
• We are looking for a clean, modern, and professional design. This includes a logo, homepage, and internal page if it will differ from the homepage.
Nice to have
• It would be excellent if you could provide an HTML mockup if your design is chosen.
Should not have
• Flash, excessive bells and whistles

```html
<!DOCTYPE html>
<html lang="en">
<head>
<meta charset="utf-8">
<title>VantaLume — Opinion Mining</title>
<link rel="stylesheet" href="https://fonts.googleapis.com/css2?family=Lato:wght@400;700&family=Open+Sans:wght@400;600&display=swap">
<style>
  :root {
    --brand-blue: #1d5a9e;
    --nav-blue: #1f5c9a;
    --link-blue: #1a4f86;
    --hero-top: #3ab9f3;
    --hero-mid: #1f8ad8;
    --hero-bottom: #0d3f86;
    --text-grey: #555;
    --panel-bg: #f4f4f4;
    --panel-border: #e2e2e2;
    --footer-bg: #333333;
    --footer-text: #bdbdbd;
    --cta-top: #ffe04a;
    --cta-bottom: #f6b90f;
  }
  * { box-sizing: border-box; margin: 0; padding: 0; }
  html, body { width: 1023px; height: 1200px; overflow: hidden; background: #fff; }
  body { position: relative; font-family: "Open Sans", sans-serif; color: var(--text-grey); }

  .site-header { position: absolute; top: 0; left: 0; width: 1023px; height: 115px;
    background: linear-gradient(#ffffff 55%, #ececec); }
  .brand { position: absolute; left: 42px; top: 32px; display: flex; align-items: center; gap: 10px; }
  .brand-mark { width: 26px; height: 26px; background: var(--brand-blue); }
  .brand-name { font-family: "Lato", sans-serif; font-size: 36px; font-weight: 400; color: #3a3a3a; letter-spacing: -0.5px; }
  .main-nav { position: absolute; top: 42px; right: 51px; display: flex; gap: 34px; }
  .main-nav a { font-family: "Lato", sans-serif; font-weight: 700; font-size: 15px; color: var(--nav-blue); text-decoration: none; }

  .hero { position: absolute; top: 115px; left: 0; width: 1023px; height: 354px;
    background: linear-gradient(180deg, var(--hero-top) 0%, var(--hero-mid) 38%, var(--hero-bottom) 100%);
    border-bottom: 2px solid #0a2c5e; }
  .hero-title { position: absolute; left: 42px; top: 38px; width: 470px; font-family: "Lato", sans-serif;
    font-weight: 700; font-size: 33px; line-height: 43px; color: #fff; }
  .hero-text { position: absolute; left: 42px; top: 126px; width: 450px; font-size: 16.5px; line-height: 32.5px;
    color: #fff; letter-spacing: 0.3px; }
  .hero-visual { position: absolute; left: 515px; top: 8px; width: 392px; height: 350px;
    border-radius: 20px; background: radial-gradient(ellipse at 50% 55%, #dfe7ef 0%, #b8c8d8 40%, rgba(120,160,210,0) 72%); }

  .panel { position: absolute; background: linear-gradient(#f1f1f1, #fafafa); border: 1px solid var(--panel-border); padding: 10px 9px; }
  .panel-title { font-family: "Lato", sans-serif; font-weight: 700; font-size: 16px; color: var(--brand-blue); margin-bottom: 18px; }
  .panel p { font-size: 12.5px; line-height: 20px; }
  .news-date { color: var(--link-blue); }
  .read-more { color: var(--link-blue); text-decoration: underline; }
  .news-item + .news-item { margin-top: 40px; }

  .news { left: 40px; top: 487px; width: 219px; height: 274px; }
  .call-to-action { left: 40px; top: 788px; width: 219px; height: 238px; }
  .case-studies { left: 760px; top: 485px; width: 219px; height: 255px; padding: 14px 10px; }
  .case-studies p .accent, .search-box p .accent { color: #173f66; }
  .contact-button { display: block; margin: 10px 0 0 -5px; width: 177px; height: 35px; border: 1px solid #e0a40a;
    background: linear-gradient(var(--cta-top), var(--cta-bottom)); color: #fff; font-family: "Lato", sans-serif;
    font-weight: 700; font-size: 15px; text-align: center; line-height: 33px; text-decoration: none; }
  .search-box { left: 760px; top: 757px; width: 219px; height: 252px; padding: 12px 9px; }
  .search-name { font-family: "Lato", sans-serif; font-size: 24px; color: #2a9fd6; margin-bottom: 8px; }
  .search-field { width: 203px; height: 32px; background: #fff; border: 1px solid #d4d4d4; margin-bottom: 20px; }

  .primary { position: absolute; left: 281px; top: 497px; width: 458px; }
  .primary-title { font-family: "Lato", sans-serif; font-weight: 700; font-size: 16px; color: var(--brand-blue); margin-bottom: 24px; }
  .primary p { font-size: 12.5px; line-height: 20px; }
  .primary p + p { margin-top: 20px; }
  .primary-photo { float: right; width: 218px; height: 145px; margin: -14px 3px 8px 10px;
    background: linear-gradient(135deg, #cfd3d8, #8d949c 55%, #e9ebee); }
  .feature-list { position: absolute; left: 281px; top: 798px; list-style: none; }
  .feature-list li { display: flex; align-items: center; gap: 8px; font-size: 13px; line-height: 22px; color: #444; }

  .site-footer { position: absolute; top: 1057px; left: 0; width: 1023px; height: 143px; background: var(--footer-bg); }
  .copyright { position: absolute; left: 46px; top: 23px; font-size: 11px; color: #9a9a9a; }
  .footer-nav { position: absolute; right: 55px; top: 21px; display: flex; gap: 22px; font-size: 12px; color: var(--footer-text); }
  .footer-nav a { color: var(--footer-text); text-decoration: none; }
</style>
</head>
<body>
  <header class="site-header">
    <div class="brand"><span class="brand-mark"></span><span class="brand-name">VantaLume</span></div>
    <nav class="main-nav">
      <a href="#">Home</a><a href="#">About Us</a><a href="#">Features</a><a href="#">Case Studies</a><a href="#">Contact Us</a>
    </nav>
  </header>

  <section class="hero">
    <h1 class="hero-title">Lorem ipsum dolor sit amet, consectetur adipiscing elit.</h1>
    <p class="hero-text">Etiam scelerisque elit sed mi laoreet tempus. Cras risus mauris, laoreet ut scelerisque a, sagittis non augue. Lorem ipsum dolor sit amet, consectetur adipiscing elit.</p>
    <div class="hero-visual" role="img" aria-label="Illustration of a colourful 3D bar chart on a grid with a magnifying glass"></div>
  </section>

  <aside class="panel news">
    <h2 class="panel-title">News</h2>
    <div class="news-item">
      <p><span class="news-date">14 May 2010</span>&nbsp; Consectetur adipiscing elit. Nunc at ligula sed purus blandit egestas ut eu nulla.<br>&gt; <a class="read-more" href="#">Read More</a></p>
    </div>
    <div class="news-item">
      <p><span class="news-date">1 April 2010</span>&nbsp; Lorem ipsum dolor sit amet consectetur elit. Nunc at ligula sed purus blandit egestas ut eu nulla.<br>&gt; <a class="read-more" href="#">Read More</a></p>
    </div>
  </aside>

  <aside class="panel call-to-action">
    <h2 class="panel-title">Call to Action</h2>
    <p>Lorem ipsum dolor sit amet, consectetur adipiscing elit. Nunc at ligula sed purus blandit egestas ut eu nulla. Etiam scelerisque elit sed mi laoreet tempus. Cras risus mauris, laoreet ut scelerisque a, sagittis non augue.</p>
  </aside>

  <main class="primary">
    <h2 class="primary-title">Primary Business Desciption</h2>
    <div class="primary-photo" role="img" aria-label="Photo of a business meeting with documents on a table"></div>
    <p>Lorem ipsum dolor sit amet, consectetur adipiscing elit. Nunc at ligula sed purus blandit egestas ut eu nulla. Etiam scelerisque elit sed mi laoreet tempus. Cras risus mauris, laoreet ut scelerisque a, sagittis non augue. Lorem ipsum dolor sit amet, consectetur adipiscing elit.</p>
    <p>Nunc at ligula sed purus blandit egestas ut eu nulla. Etiam scelerisque elit sed mi laoreet tempus. Cras risus mauris, laoreet ut scelerisque a, sagittis non augue. ut eu nulla.</p>
  </main>

  <ul class="feature-list">
    <li><svg width="12" height="10" viewBox="0 0 12 10"><path d="M0 3h6V0l6 5-6 5V7H0z" fill="#2f6fb0"/></svg>Morbi venenatis dolor non magna rutrum</li>
    <li><svg width="12" height="10" viewBox="0 0 12 10"><path d="M0 3h6V0l6 5-6 5V7H0z" fill="#2f6fb0"/></svg>Sed vehicula ornare tortor</li>
    <li><svg width="12" height="10" viewBox="0 0 12 10"><path d="M0 3h6V0l6 5-6 5V7H0z" fill="#2f6fb0"/></svg>Pellentesque vel neque ut ipsum convallis</li>
    <li><svg width="12" height="10" viewBox="0 0 12 10"><path d="M0 3h6V0l6 5-6 5V7H0z" fill="#2f6fb0"/></svg>Aenean quam risus</li>
    <li><svg width="12" height="10" viewBox="0 0 12 10"><path d="M0 3h6V0l6 5-6 5V7H0z" fill="#2f6fb0"/></svg>Integer ullamcorper posuere nulla ac ultrices</li>
  </ul>

  <aside class="panel case-studies">
    <h2 class="panel-title">Case Studies</h2>
    <p>Lorem ipsum dolor sit amet, consectetur adipiscing elit. Nunc at ligula sed <span class="accent">purus blandit egestas</span> ut eu nulla. Etiam scelerisEtiam scelerisque elit sed mi laoreet tempus.<br>&gt; <a class="read-more" href="#">Read More</a></p>
    <a class="contact-button" href="#">CONTACT US</a>
  </aside>

  <aside class="panel search-box">
    <div class="search-name">Seekly</div>
    <div class="search-field"></div>
    <p>Lorem ipsum dolor sit amet, consectetur adipiscing elit. Nunc at ligula sed <span class="accent">purus blandit egestas</span> ut eu nulla.</p>
  </aside>

  <footer class="site-footer">
    <p class="copyright">Copyright VantaLume &nbsp; All Rights Reserved</p>
    <nav class="footer-nav">
      <a href="#">Home</a><span>/</span><a href="#">About Us</a><span>/</span><a href="#">Features</a><span>/</span><a href="#">Case Studies</a><span>/</span><a href="#">Contact Us</a>
    </nav>
  </footer>
</body>
</html>
```